Business Stationary, Letterhead, Fax Cover Sheet, Client Intake, Email Signature, Thank you cards.
Marwick Law Firm
Business Stationary, Letterhead, Fax Cover Sheet, Client Intake, Email Signature, Thank you cards. - Law
Creative Brief
Professional
Len Marwick
Lawyer
2837 Falbrook St., Suite 1940 Houston, Texas 77014
len@marwick-law.example
www.marwick-law.example
Please note this project is Not for just One Person but for All Staff. The files should be in editable format to allow for different names and titles on cards.

```html
<!DOCTYPE html>
<html lang="en">
<head>
<meta charset="utf-8">
<title>Marwick Law Firm – Email Signatures</title>
<link href="https://fonts.googleapis.com/css2?family=Arimo:wght@400;700&display=swap" rel="stylesheet">
<style>
  :root {
    --stage: #e8e5e0;
    --paper: #ffffff;
    --navy: #1c2a8c;
    --band-edge: #4a5ad0;
    --ink: #1e1e1e;
    --muted: #555a66;
    --rule: #c9ccd4;
    --faint: #e3e6f1;
  }
  * { margin: 0; padding: 0; box-sizing: border-box; }
  html, body { width: 1200px; height: 518px; overflow: hidden; }
  body {
    background: var(--stage);
    font-family: "Arimo", Arial, sans-serif;
    color: var(--ink);
    position: relative;
  }
  .signature {
    position: absolute;
    left: 48px;
    width: 1104px;
    background: var(--paper);
    box-shadow: 0 2px 6px rgba(0,0,0,.12);
    overflow: hidden;
  }
  .signature--classic { top: 118px; height: 180px; }
  .signature--banded  { top: 312px; height: 180px; }

  .firm-name {
    position: absolute;
    display: flex;
    align-items: center;
    gap: 14px;
    font-family: "Arimo", Arial, sans-serif;
    font-weight: 700;
    font-size: 30px;
    color: var(--ink);
  }
  .firm-name .mark {
    width: 40px; height: 40px;
    border-radius: 50%;
    background: var(--navy);
    flex: none;
  }
  .signature--classic .firm-name { left: 40px; top: 68px; }
  .signature--banded .firm-name  { left: 40px; top: 52px; }

  .divider {
    position: absolute;
    top: 36px; bottom: 36px;
    left: 470px;
    width: 1px;
    background: var(--rule);
  }
  .person { position: absolute; }
  .person .name { font-size: 30px; font-weight: 700; color: var(--ink); }
  .person .title { font-size: 16px; color: var(--muted); margin-top: 6px; }
  .signature--classic .person { left: 500px; top: 62px; }
  .signature--banded .person  { left: 500px; top: 28px; }

  .contact { position: absolute; font-size: 11px; line-height: 1.55; color: var(--ink); }
  .contact b { font-weight: 700; }
  .signature--classic .contact { left: 745px; top: 42px; }
  .signature--banded .address  { left: 500px; top: 100px; }
  .signature--banded .lines    { left: 745px; top: 82px; }

  .accent {
    position: absolute;
    right: 24px;
    width: 110px; height: 110px;
    border-radius: 50%;
    background: var(--faint);
  }
  .signature--classic .accent { top: 35px; }
  .signature--banded .accent  { top: 18px; }

  .web-band {
    position: absolute;
    left: 0; right: 0; bottom: 0;
    height: 26px;
    background: var(--navy);
    border-top: 4px solid var(--band-edge);
    color: #fff;
    font-size: 12px;
    font-weight: 700;
    letter-spacing: 3px;
    text-align: center;
    line-height: 22px;
  }
</style>
</head>
<body>

<section class="signature signature--classic">
  <div class="firm-name"><span class="mark"></span>Marwick Law Firm</div>
  <div class="divider"></div>
  <div class="person">
    <div class="name">Len Marwick</div>
    <div class="title">Lawyer</div>
  </div>
  <div class="contact">
    2837 Falbrook St., Suite 1940<br>
    Houston, Texas 77014<br>
    <b>Phone:</b> 713-555-0244<br>
    <b>Fax:</b> 713-555-0250<br>
    <b>Email:</b> len@marwick-law.example<br>
    <b>Web:</b> www.marwick-law.example
  </div>
  <div class="accent"></div>
</section>

<section class="signature signature--banded">
  <div class="firm-name"><span class="mark"></span>Marwick Law Firm</div>
  <div class="divider"></div>
  <div class="person">
    <div class="name">Len Marwick</div>
    <div class="title">Lawyer</div>
  </div>
  <div class="contact address">
    2837 Falbrook St., Suite 1940<br>
    Houston, Texas 77014
  </div>
  <div class="contact lines">
    <b>Phone:</b> 713-555-0244<br>
    <b>Fax:</b> 713-555-0250<br>
    <b>Email:</b> len@marwick-law.example
  </div>
  <div class="accent"></div>
  <div class="web-band">www.marwick-law.example</div>
</section>

</body>
</html>
```